Business Card Design needed for logo design project

Our company needs a Business Card Design. Please refer to our original project in the link above.

Industry/Entity Type

Business

```html
<!DOCTYPE html>
<html lang="en">
<head>
<meta charset="utf-8">
<title>Morvane Coastal — Business Card</title>
<link rel="stylesheet" href="https://fonts.googleapis.com/css2?family=Arimo:wght@400&display=swap">
<style>
  :root {
    --bg: #dcdcdc;
    --card: #ffffff;
    --ink: #1f1f1f;
    --accent: #3f83c8;
    --blue-deep: #2f4fa8;
    --blue-mid: #2a7fd0;
    --blue-sky: #3fb2ea;
    --lavender: #d9d6ee;
    --teal: #2a8a7a;
  }
  * { margin: 0; padding: 0; box-sizing: border-box; }
  html, body {
    width: 1200px; height: 1200px; overflow: hidden;
    background: var(--bg);
    font-family: "Arimo", Arial, sans-serif;
  }
  .card {
    position: absolute;
    left: 263px;
    width: 674px;
    height: 375px;
    background: var(--card);
    overflow: hidden;
  }
  .card--front { top: 185px; }
  .card--back { top: 636px; }

  .front-art {
    position: absolute; inset: 0;
    background:
      linear-gradient(200deg, rgba(63,178,234,0) 55%, rgba(63,178,234,.55) 80%, rgba(42,138,122,.5) 100%),
      linear-gradient(100deg, #ffffff 0%, #f3f2fa 10%, var(--lavender) 22%, #6e8fd6 36%, var(--blue-deep) 50%, var(--blue-mid) 68%, #4d8fd8 85%, var(--blue-sky) 100%);
  }
  .front-brand {
    position: absolute;
    left: 282px; top: 148px;
    color: #ffffff;
  }
  .brand-row { display: flex; align-items: center; gap: 14px; }
  .brand-mark {
    width: 22px; height: 22px;
    background: currentColor;
  }
  .brand-name {
    font-size: 34px; font-weight: 400; letter-spacing: .5px;
    line-height: 1;
  }
  .brand-tagline {
    margin-top: 8px; margin-left: 36px;
    font-size: 11px;
  }

  .back-art {
    position: absolute; inset: 0;
    background: linear-gradient(200deg, var(--blue-deep) 0%, var(--blue-mid) 22%, #7aa6de 45%, var(--lavender) 70%, #ffffff 100%);
    clip-path: polygon(367px 0, 674px 0, 674px 375px, 565px 375px, 565px 200px);
  }
  .back-brand {
    position: absolute;
    left: 30px; top: 52px;
    color: var(--ink);
  }
  .back-brand .brand-mark { background: var(--accent); width: 20px; height: 20px; }
  .back-brand .brand-name { font-size: 28px; }
  .back-brand .brand-tagline { margin-left: 34px; font-size: 9px; margin-top: 6px; }

  .person-name {
    position: absolute; left: 85px; top: 184px;
    font-size: 28px; font-weight: 400; color: var(--accent);
  }
  .contact-list {
    position: absolute; left: 87px; top: 236px;
    list-style: none;
    font-size: 18px; line-height: 27px; color: var(--ink);
  }
</style>
</head>
<body>
  <section class="card card--front">
    <div class="front-art" role="img" aria-label="Abstract faceted geometric shards in blue and lavender tones"></div>
    <div class="front-brand">
      <div class="brand-row">
        <span class="brand-mark"></span>
        <span class="brand-name">Morvane Coastal</span>
      </div>
      <p class="brand-tagline">Your Trusted Real Estate Advisors</p>
    </div>
  </section>

  <section class="card card--back">
    <div class="back-art" role="img" aria-label="Abstract faceted geometric shards in blue and lavender tones"></div>
    <div class="back-brand">
      <div class="brand-row">
        <span class="brand-mark"></span>
        <span class="brand-name">Morvane Coastal</span>
      </div>
      <p class="brand-tagline">Your Trusted Real Estate Advisors</p>
    </div>
    <h1 class="person-name">Idris Falcone</h1>
    <ul class="contact-list">
      <li>555-014-782</li>
      <li>idris@morvanecoastal.com</li>
      <li>morvanecoastal.com</li>
    </ul>
  </section>
</body>
</html>
```